Life Coaching Business - needs business card design with logo

I need a business card and logo design for a life coaching business I started based in Los Angeles. I offer services to clients that wish to bring more balance and overall wholeness to their lives. As of right now, the business name is "Marcus Elwood Coaching." An iidea I had for the logo was to be kind of a Yin-Yang symbol but with dolphins, as the dolphin has symbolic meaning for my business. Although I am really open to other ideas as long as it incorporates the idea of “balance,” “wholeness,” and “dolphins.”I also wanted to incorporate the color blue, maybe in the form of water, waves, or some sort of peaceful imagery.

```html
<!DOCTYPE html>
<html lang="en">
<head>
<meta charset="utf-8">
<title>Marcus Elwood Coaching – Business Card</title>
<link rel="stylesheet" href="https://fonts.googleapis.com/css2?family=Noto+Serif:wght@400;700&display=swap">
<style>
  :root {
    --backdrop: #3f3f3f;
    --navy: #06558a;
    --ink: #134f85;
    --sky: #40c4ef;
    --white: #ffffff;
  }
  * { margin: 0; padding: 0; box-sizing: border-box; }
  html, body { width: 1189px; height: 1200px; overflow: hidden; }
  body {
    background: var(--backdrop);
    font-family: "Noto Serif", Georgia, serif;
    position: relative;
  }
  .card {
    position: absolute;
    top: 202px;
    width: 437px;
    height: 764px;
    overflow: hidden;
  }
  .card-front { left: 141px; background: var(--white); border-radius: 57px 0 57px 0; }
  .card-back { left: 597px; background: var(--navy); border-radius: 0 57px 0 57px; }
  .card-art { position: absolute; inset: 0; }
  .centered { position: absolute; left: 0; right: 0; text-align: center; }

  .brand-mark { position: absolute; }
  .brand-name {
    font-weight: 700;
    line-height: 1.1;
    letter-spacing: 0.5px;
  }
  .card-front .brand-name { top: 244px; font-size: 30px; color: var(--ink); }
  .card-back .brand-name { top: 606px; font-size: 34px; color: var(--white); }

  .person-name { top: 470px; font-size: 27px; font-weight: 700; color: var(--white); }
  .person-title { top: 505px; font-size: 19px; color: var(--white); }
  .contact-icon { position: absolute; left: 200px; width: 37px; height: 37px; }
  .contact-text { font-size: 19px; color: var(--white); }
  .phone-text { top: 575px; }
  .email-text { top: 656px; }
  .website { top: 726px; font-size: 19px; color: var(--white); letter-spacing: 0.5px; }
</style>
</head>
<body>
  <section class="card card-front">
    <svg class="card-art" viewBox="0 0 437 764" aria-hidden="true">
      <path d="M0 445 C120 382 320 362 437 420 L437 764 L0 764 Z" fill="var(--sky)"/>
      <path d="M0 462 C130 405 300 392 437 426 L437 764 L0 764 Z" fill="var(--navy)"/>
      <path d="M85 437 C200 405 330 400 437 426" fill="none" stroke="var(--white)" stroke-width="3"/>
      <rect x="0" y="709" width="437" height="4" fill="var(--white)"/>
      <rect x="0" y="713" width="437" height="51" fill="var(--sky)"/>
      <line x1="68" y1="608" x2="370" y2="608" stroke="#9fb7cc" stroke-width="1"/>
    </svg>

    <svg class="brand-mark" style="left:167px;top:100px" width="102" height="102" viewBox="0 0 102 102" aria-hidden="true">
      <circle cx="51" cy="51" r="50" fill="var(--navy)"/>
    </svg>
    <p class="centered brand-name">MARCUS ELWOOD<br>COACHING</p>

    <p class="centered person-name">Marcus Elwood</p>
    <p class="centered person-title">Director of Operations</p>

    <svg class="contact-icon" style="top:531px" viewBox="0 0 37 37" aria-hidden="true">
      <circle cx="18.5" cy="18.5" r="17" fill="var(--white)" stroke="var(--sky)" stroke-width="3"/>
      <path d="M10 15 Q18.5 9 27 15 L25 18 L22 16.5 L22 14.5 Q18.5 13 15 14.5 L15 16.5 L12 18 Z M13 19 L24 19 L26 26 L11 26 Z" fill="var(--navy)"/>
    </svg>
    <p class="centered contact-text phone-text">555.555.5555</p>

    <svg class="contact-icon" style="top:620px" viewBox="0 0 37 37" aria-hidden="true">
      <circle cx="18.5" cy="18.5" r="17" fill="var(--white)" stroke="var(--sky)" stroke-width="3"/>
      <rect x="10" y="12" width="17" height="13" fill="var(--navy)"/>
      <path d="M10 12 L18.5 19.5 L27 12 M10 25 L16 18 M27 25 L21 18" fill="none" stroke="var(--white)" stroke-width="1.4"/>
    </svg>
    <p class="centered contact-text email-text">hello@elwoodcoach.com</p>

    <p class="centered website">www.ELWOODCOACH.com</p>
  </section>

  <section class="card card-back">
    <svg class="card-art" viewBox="0 0 437 764" aria-hidden="true">
      <circle cx="211" cy="239" r="220" fill="var(--white)"/>
    </svg>
    <p class="centered brand-name">MARCUS ELWOOD<br>COACHING</p>
  </section>
</body>
</html>
```